Varlowe Supply Partners
Business Cards and Stationary
Project: Varlowe Supply Partners
Varlowe Supply Partners -
Creative Brief
Professional
Daniel Varlowe
Manufacturer's Representative
20375 82nd Lane NW Elk Ridge, MN 55492
dvarlowe@varlowesupply-example.com
www.varlowesupply-example.com

```html
<!DOCTYPE html>
<html lang="en">
<head>
<meta charset="utf-8">
<title>Varlowe Supply Partners – Stationery</title>
<link rel="stylesheet" href="https://fonts.googleapis.com/css2?family=Open+Sans:wght@400;600&display=swap">
<style>
  :root {
    --backdrop: #e4e2df;
    --paper: #ffffff;
    --navy: #1d3a6b;
    --band-top: #7fa6d6;
    --band-bottom: #152e5c;
    --ink: #333a44;
    --muted: #5a626c;
    --rule: #9aa3ad;
  }
  * { box-sizing: border-box; margin: 0; padding: 0; }
  html, body { width: 1200px; height: 492px; overflow: hidden; }
  body {
    position: relative;
    background: var(--backdrop);
    font-family: "Open Sans", Arial, sans-serif;
    color: var(--ink);
  }
  address { font-style: normal; }
  .sheet, .envelope, .card {
    position: absolute;
    background: var(--paper);
    box-shadow: 0 2px 6px rgba(0,0,0,.18);
    overflow: hidden;
  }
  .band {
    position: absolute; top: 0; bottom: 0; left: 0;
    background: linear-gradient(180deg, var(--band-top) 0%, #3f6aa6 45%, var(--band-bottom) 100%);
  }
  .brand {
    position: absolute;
    display: flex; align-items: center; gap: 4px;
    font-weight: 600; color: var(--navy); white-space: nowrap;
  }
  .brand-dot { border-radius: 50%; background: var(--navy); flex: none; }

  /* letter-size sheets */
  .sheet { top: 24px; width: 324px; height: 437px; }
  .sheet .band { width: 22px; }
  .sheet .brand { top: 20px; left: 34px; font-size: 8px; }
  .sheet .brand-dot { width: 9px; height: 9px; }
  .sheet-contact {
    position: absolute; top: 16px; left: 160px;
    font-size: 4px; line-height: 5.6px; color: var(--muted);
  }
  .fax { left: 67px; }
  .letterhead { left: 413px; }
  .fax-title { position: absolute; top: 120px; left: 40px; font-size: 22px; font-weight: 400; color: #222; }
  .fax-form {
    position: absolute; top: 146px; left: 40px; right: 18px;
    display: grid; grid-template-columns: 1fr 1fr; column-gap: 30px;
  }
  .fax-field {
    font-size: 4.5px; color: #444; height: 16px;
    border-bottom: 1px solid var(--rule);
    display: flex; align-items: flex-end; padding-bottom: 2px;
  }
  .fax-options {
    position: absolute; top: 222px; left: 40px; right: 18px;
    display: flex; justify-content: space-between; font-size: 4.5px; color: #444;
  }
  .fax-option { display: flex; align-items: center; gap: 3px; }
  .box { width: 5px; height: 5px; border: 1px solid #666; }
  .letter-footer {
    position: absolute; bottom: 20px; left: 34px;
    font-size: 4px; line-height: 5.6px; color: var(--muted);
  }

  /* envelopes */
  .envelope-back { left: 806px; top: 53px; width: 346px; height: 211px; background: #f7f8fa; }
  .envelope-back svg { position: absolute; inset: 0; }
  .envelope-back .brand { top: 14px; left: 50%; transform: translateX(-50%); font-size: 8px; }
  .envelope-back .brand-dot { width: 8px; height: 8px; }
  .envelope-front { left: 758px; top: 149px; width: 356px; height: 189px; }
  .envelope-front .band { width: 22px; }
  .envelope-front .brand { top: 20px; left: 32px; font-size: 8px; }
  .envelope-front .brand-dot { width: 8px; height: 8px; }
  .return-address {
    position: absolute; top: 34px; left: 32px;
    font-size: 4px; line-height: 5.6px; color: var(--muted);
  }

  /* business cards */
  .card { top: 367px; width: 125px; height: 65px; border-radius: 2px; }
  .card-front { left: 809px; }
  .card-front .band { width: 10px; }
  .card-front .brand { top: 8px; left: 16px; font-size: 5.5px; gap: 3px; }
  .card-front .brand-dot { width: 6px; height: 6px; }
  .card-person { position: absolute; top: 22px; left: 16px; font-size: 4.2px; line-height: 5.4px; }
  .card-person strong { font-weight: 600; color: var(--navy); }
  .card-details { position: absolute; bottom: 6px; left: 16px; font-size: 3.3px; line-height: 4.4px; color: var(--muted); }
  .card-back {
    left: 953px; width: 127px; height: 63px;
    background: radial-gradient(ellipse at 50% 40%, #3b67a6 0%, var(--band-bottom) 80%);
  }
  .card-back .brand { top: 50%; left: 50%; transform: translate(-50%, -50%); font-size: 5.5px; color: #ffffff; gap: 3px; }
  .card-back .brand-dot { width: 6px; height: 6px; background: #ffffff; }
</style>
</head>
<body>

  <section class="sheet fax" aria-label="Fax cover sheet">
    <div class="band"></div>
    <div class="brand"><span class="brand-dot"></span>Varlowe Supply Partners</div>
    <address class="sheet-contact">
      P 763.555.0148 F 763.555.0149<br>
      20375 82nd Lane NW Elk Ridge, MN 55492<br>
      dvarlowe@varlowesupply-example.com<br>
      www.varlowesupply-example.com
    </address>
    <h1 class="fax-title">FAX</h1>
    <div class="fax-form">
      <div class="fax-field">To:</div><div class="fax-field">From:</div>
      <div class="fax-field">Fax:</div><div class="fax-field">Pages:</div>
      <div class="fax-field">Phone:</div><div class="fax-field">Date:</div>
      <div class="fax-field">Re:</div><div class="fax-field">CC:</div>
    </div>
    <div class="fax-options">
      <span class="fax-option"><span class="box"></span>Urgent</span>
      <span class="fax-option"><span class="box"></span>For Review</span>
      <span class="fax-option"><span class="box"></span>Please Comment</span>
      <span class="fax-option"><span class="box"></span>Please Reply</span>
      <span class="fax-option"><span class="box"></span>Please Recycle</span>
    </div>
  </section>

  <section class="sheet letterhead" aria-label="Letterhead">
    <div class="band"></div>
    <div class="brand"><span class="brand-dot"></span>Varlowe Supply Partners</div>
    <address class="letter-footer">
      P 763.555.0148 F 763.555.0149 · dvarlowe@varlowesupply-example.com<br>
      20375 82nd Lane NW Elk Ridge, MN 55492 · www.varlowesupply-example.com
    </address>
  </section>

  <section class="envelope envelope-back" aria-label="Envelope back">
    <svg viewBox="0 0 346 211" preserveAspectRatio="none" aria-hidden="true">
      <polyline points="0,0 173,110 346,0" fill="none" stroke="#d5d9df" stroke-width="1.5"/>
      <line x1="0" y1="211" x2="140" y2="98" stroke="#e2e5ea" stroke-width="1"/>
      <line x1="346" y1="211" x2="206" y2="98" stroke="#e2e5ea" stroke-width="1"/>
    </svg>
    <div class="brand"><span class="brand-dot"></span>Varlowe Supply Partners</div>
  </section>

  <section class="envelope envelope-front" aria-label="Envelope front">
    <div class="band"></div>
    <div class="brand"><span class="brand-dot"></span>Varlowe Supply Partners</div>
    <address class="return-address">
      20375 82nd Lane NW<br>
      Elk Ridge, MN 55492
    </address>
  </section>

  <section class="card card-front" aria-label="Business card front">
    <div class="band"></div>
    <div class="brand"><span class="brand-dot"></span>Varlowe Supply Partners</div>
    <p class="card-person"><strong>Daniel Varlowe</strong><br>Manufacturer's Representative</p>
    <address class="card-details">
      P 763.555.0148<br>
      20375 82nd Lane NW Elk Ridge, MN 55492<br>
      dvarlowe@varlowesupply-example.com<br>
      www.varlowesupply-example.com
    </address>
  </section>

  <section class="card card-back" aria-label="Business card back">
    <div class="brand"><span class="brand-dot"></span>Varlowe Supply Partners</div>
  </section>

</body>
</html>
```